Horse Training Book Cover Design

We have had some book covers drafted by some freelancers on Gigbrook, but they just miss the mark a little bit.
This book is a Horse Training Book, but also entails a lot of mindfulness and attunement practices. Focus on effective Fonts.
We will be using Tallow Presswell. We want a paperback and hardback cover.
Specs: 5.50 x 8.50 inches
Pages: 250
I have uploaded the Gigbrook drafts as well as some drafts that I have made. We're looking for a tooled leather look, we want the title to look as if it was stamped into the leather background, but also make it easy to read the back print. I have attached multiple inspirations, but we don't just want you to use these, we want you to create something unique from them.
FRONT COVER TEXT
Title: The Foundations of Schooling
Subtitle: Understanding the relationship between you and your horse, and why effective training works.
Author: Dorian Halvesty
BACK COVER TEXT
Quote: “As to methods there may be a million and then some, but Principles are few. The man who grasps principles can successfully select his own methods. The man who tries methods, ignoring principles, is sure to have trouble.” - Bartholomew Quince Early 20th Century Efficiency Expert
Book Overview: In The Foundations of Schooling, Dorian Halvesty describes the 12 principles that all successful horsemen and women use to effectively train horses. After 30 years of training, Dorian discovered a 13th principle that, when integrated with the others, makes you the best person to train your horse.
Book Review: “Dorian has a unique ability to understand both horse and rider from the inside out as he helps them individually - and together. Strong relationships come from trust and perceiving the other from their point of view. Horses do this naturally; fortunately for us, Dorian gives us humans the tools to understand ourselves and our horses.”
-Lorna Pettigrew, Prairie Riders Honor Roll Inductee
Horse Owners
Education, Animals and Pets

```html
<!DOCTYPE html>
<html lang="en">
<head>
<meta charset="utf-8">
<title>The Foundations of Schooling – Cover Spread</title>
<link rel="stylesheet" href="https://fonts.googleapis.com/css2?family=Almendra:wght@400;700&display=swap">
<style>
:root{
  --page:#ffffff;
  --leather:#5a5152;
  --leather-light:#625a5b;
  --leather-dark:#4a4344;
  --ink:#1d1919;
  --highlight:rgba(255,255,255,.14);
  --figure:#2b2526;
}
*{margin:0;padding:0;box-sizing:border-box}
html,body{width:1200px;height:843px;overflow:hidden;background:var(--page)}
body{position:relative;font-family:"Almendra",serif;color:var(--ink)}
.cover{
  position:absolute;top:70px;width:551px;height:709px;
  background:radial-gradient(ellipse at 50% 45%,var(--leather-light),var(--leather) 60%,var(--leather-dark));
}
.cover--front{left:32px}
.cover--back{left:604px}
.frame-outer{
  position:absolute;left:19px;top:24px;right:19px;bottom:14px;
  border:3px solid var(--ink);
  box-shadow:0 1px 0 var(--highlight),inset 0 1px 0 var(--highlight);
}
.frame-inner{
  position:absolute;left:52px;top:58px;right:50px;bottom:43px;
  border:3px solid var(--ink);
  box-shadow:0 1px 0 var(--highlight),inset 0 0 10px rgba(0,0,0,.45);
}
.stamped{text-shadow:0 1px 0 var(--highlight),0 -1px 1px rgba(0,0,0,.45)}
.centered{position:absolute;left:0;right:0;text-align:center}
.title{top:100px;left:62px;right:60px;font-size:28px;font-weight:700;white-space:nowrap}
.rule{height:2px;background:var(--ink);box-shadow:0 1px 0 var(--highlight)}
.front-rule{position:absolute;left:134px;width:282px;top:149px}
.subtitle{top:158px;left:118px;right:118px;font-size:18px;font-weight:700;line-height:23px}
.illustration{position:absolute;border-radius:40% 40% 8% 8%;
  background:radial-gradient(ellipse at 50% 55%,var(--figure),rgba(43,37,38,.35) 75%,transparent)}
.illustration--trainer{left:57px;top:341px;width:116px;height:320px}
.illustration--horse{left:283px;top:406px;width:216px;height:260px}
.author{top:664px;font-size:19px;font-weight:700}
.back-content{
  position:absolute;left:72px;right:70px;top:122px;
  display:flex;flex-direction:column;align-items:center;text-align:center;
}
.back-text{font-size:16px;line-height:20.2px}
.back-rule{width:280px;margin-top:6px}
.attribution{font-size:11px;font-weight:700;line-height:14px;margin-top:7px;max-width:280px}
.overview{margin-top:28px}
.review{margin-top:34px}
</style>
</head>
<body>
  <section class="cover cover--front" aria-label="Front cover">
    <div class="frame-outer"></div>
    <div class="frame-inner"></div>
    <h1 class="centered title stamped">The Foundations of Schooling</h1>
    <div class="rule front-rule"></div>
    <p class="centered subtitle stamped">Understanding the relationship between you and your horse, and why effective training works.</p>
    <div class="illustration illustration--trainer" role="img" aria-label="Silhouette of a trainer raising a long whip"></div>
    <div class="illustration illustration--horse" role="img" aria-label="Illustration of a rearing paint horse"></div>
    <p class="centered author stamped">Dorian Halvesty</p>
  </section>

  <section class="cover cover--back" aria-label="Back cover">
    <div class="frame-outer"></div>
    <div class="frame-inner"></div>
    <div class="back-content">
      <p class="back-text quote stamped">“As to methods there may be a million and then some, but Principles are few. The man who grasps principles can successfully select his own methods. The man who tries methods, ignoring principles, is sure to have trouble.”</p>
      <div class="rule back-rule"></div>
      <p class="attribution stamped">Bartholomew Quince Early 20th Century Efficiency Expert</p>
      <p class="back-text overview stamped">In The Foundations of Schooling, Dorian Halvesty describes the 12 principles that all successful horsemen and women use to effectively train horses. After 30 years of training, Dorian discovered a 13th principle that, when integrated with the others, makes you the best person to train your horse.</p>
      <p class="back-text review stamped">“Dorian has a unique ability to understand both horse and rider from the inside out as he helps them individually - and together. Strong relationships come from trust and perceiving the other from their point of view. Horses do this naturally; fortunately for us, Dorian gives us humans the tools to understand ourselves and our horses.”</p>
      <div class="rule back-rule"></div>
      <p class="attribution stamped">Lorna Pettigrew, Prairie Riders Honor Roll Inductee</p>
    </div>
  </section>
</body>
</html>
```